ORV Holding

ORV holding is located in the UAE. In the company, there are several departments covering Hospitality management, Facility Management, interior design and Construction.

The logo should not include the name holding, Just ORV.

Needed Items:

(1) Logo.
(2) Business Card.
(3) Letterhead
(4) Envelope
(5) cd cover
(6) email signature
Updates

The previous brief was misplaced with another competition. Current update is the final.

Target Market(s)

Collaboration with international high end firms.

Industry/Entity Type

Business

Requirements
Must have
• COLOR PREFERENCE Maximum 2 colors, preferably mono-color with different shades.
Nice to have
• Elegant, luxurious, and minimalistic.

```html
<!DOCTYPE html>
<html lang="en">
<head>
<meta charset="utf-8">
<title>ORV Holding – Business Card</title>
<link rel="stylesheet" href="https://fonts.googleapis.com/css2?family=Bebas+Neue&family=Lato:wght@400&display=swap">
<style>
  :root {
    --backdrop: #2a2a2a;
    --brand-green: #4a8c25;
    --brand-red: #a50c0c;
    --back-red: #ab0000;
    --mark-red: #8a0000;
    --paper: #ffffff;
    --ink: #1e1e1e;
  }
  html, body {
    margin: 0;
    padding: 0;
    width: 1075px;
    height: 1200px;
    overflow: hidden;
    background: var(--backdrop);
  }
  .stage {
    position: relative;
    width: 1196px;
    height: 1335px;
    transform: scale(0.8988);
    transform-origin: 0 0;
  }
  .card {
    position: absolute;
    left: 229px;
    width: 738px;
    height: 438px;
    overflow: hidden;
    box-shadow: 3px 3px 4px rgba(0,0,0,0.6);
  }
  .card--front { top: 208px; background: var(--paper); }
  .card--back  { top: 709px; background: var(--back-red); }

  .card__bands { position: absolute; inset: 0; width: 100%; height: 100%; }

  .brand-name {
    position: absolute;
    font-family: "Bebas Neue", sans-serif;
    line-height: 1;
    margin: 0;
  }
  .card--front .brand-name {
    left: 60px;
    top: 96px;
    width: 180px;
    text-align: center;
    font-size: 118px;
    color: var(--brand-red);
  }
  .card--back .brand-name {
    left: 0;
    top: 140px;
    width: 100%;
    text-align: center;
    font-size: 170px;
    color: var(--mark-red);
  }

  .holder {
    position: absolute;
    right: 60px;
    top: 50px;
    text-align: right;
  }
  .holder__name {
    margin: 0;
    font-family: "Bebas Neue", sans-serif;
    font-weight: 400;
    font-size: 36px;
    line-height: 1;
    color: var(--brand-red);
  }
  .holder__surname { color: var(--brand-green); }
  .holder__role {
    margin: 4px 0 0;
    font-family: "Lato", sans-serif;
    font-size: 20px;
    color: var(--ink);
  }

  .contact {
    position: absolute;
    right: 53px;
    top: 268px;
    margin: 0;
    padding: 0;
    list-style: none;
    font-family: "Lato", sans-serif;
    font-size: 20px;
    color: var(--paper);
    text-align: right;
  }
  .contact__item {
    display: flex;
    justify-content: flex-end;
    align-items: flex-start;
    gap: 8px;
    line-height: 27.5px;
  }
  .contact__item--address { margin-top: 14px; line-height: 27px; }
  .contact__icon { width: 20px; height: 20px; margin-top: 4px; flex: none; }
</style>
</head>
<body>
<div class="stage">

  <section class="card card--front">
    <svg class="card__bands" viewBox="0 0 738 438" aria-hidden="true">
      <path d="M0,330 C220,360 420,190 738,205 L738,438 L0,438 Z" fill="var(--brand-green)"/>
      <path d="M0,292 C160,335 300,300 380,238" fill="none" stroke="var(--brand-red)" stroke-width="16"/>
    </svg>

    <p class="brand-name">ORV</p>

    <div class="holder">
      <h1 class="holder__name">Daniel <span class="holder__surname">Harper</span></h1>
      <p class="holder__role">Managing Director</p>
    </div>

    <ul class="contact">
      <li class="contact__item">044-987 654 321
        <svg class="contact__icon" viewBox="0 0 24 24"><path fill="#fff" d="M6.6 10.8a15 15 0 0 0 6.6 6.6l2.2-2.2a1 1 0 0 1 1-.25 11 11 0 0 0 3.6.6 1 1 0 0 1 1 1V20a1 1 0 0 1-1 1A17 17 0 0 1 3 4a1 1 0 0 1 1-1h3.5a1 1 0 0 1 1 1 11 11 0 0 0 .6 3.6 1 1 0 0 1-.25 1z"/></svg>
      </li>
      <li class="contact__item">info@orvmail.com
        <svg class="contact__icon" viewBox="0 0 24 24"><rect x="2" y="5" width="20" height="14" fill="#fff"/><path d="M2 5l10 8 10-8" fill="none" stroke="var(--brand-green)" stroke-width="1.6"/></svg>
      </li>
      <li class="contact__item">www.orvholding.com
        <svg class="contact__icon" viewBox="0 0 24 24"><g fill="none" stroke="#fff" stroke-width="1.8"><circle cx="12" cy="12" r="9"/><ellipse cx="12" cy="12" rx="4" ry="9"/><path d="M3 12h18M5 7h14M5 17h14"/></g></svg>
      </li>
      <li class="contact__item contact__item--address"><span>18 Harbour Road, Suite 4<br>Dubai, UAE 10245</span>
        <svg class="contact__icon" viewBox="0 0 24 24"><path fill="#fff" d="M12 2a7 7 0 0 0-7 7c0 5 7 13 7 13s7-8 7-13a7 7 0 0 0-7-7zm0 9.5A2.5 2.5 0 1 1 12 6.5a2.5 2.5 0 0 1 0 5z"/></svg>
      </li>
    </ul>
  </section>

  <section class="card card--back">
    <p class="brand-name">ORV</p>
  </section>

</div>
</body>
</html>
```